Massage Certificate Design that is Elegant, Modern, Hip with a "Pop"

We need a massage certificate for our Chiropractic office. Our brand feel is modern, clean, hip, and bold. Something that has some "pop" to it and that is different. We play dance music on Fridays, we care for kids and families, and provide vitality care, not just about neck and back pain. We would like to see a design that incorporates our logo along with a burnt orange accent color, tan, white, and black. We attached a sample certificate. On one side we would like to have it designate the massage price of $50, a space to write in who the certificate is for, who it is from, a space to write in an expiration date. On the back of the certificate we would like to have the office contact info. 4173 W. Marlow Lane, C204, Scottsdale, AZ 85260. A map of the location.
Phone: (480) 731-2946
Facebook
Twitter

Target Market(s)

Moms, Wellness Minded, Vitality Focused, Looking for reducing stress and muscle stiffness

Industry/Entity Type

Health And Wellness

Colors
f37122
000000
fefefe

Requirements
Must have
• Burnt orange accent color, tan, black, and white colors used.

```html
<!DOCTYPE html>
<html lang="en">
<head>
<meta charset="utf-8">
<title>Massage Gift Certificate</title>
<link href="https://fonts.googleapis.com/css2?family=Bebas+Neue&family=Crimson+Text:wght@400&family=Lato:wght@400;700&display=swap" rel="stylesheet">
<style>
  :root {
    --orange: #f37122;
    --orange-deep: #e0560f;
    --orange-light: #ff9a3c;
    --black: #000000;
    --ink: #1a1a1a;
    --white: #fefefe;
    --paper: #ececec;
    --backdrop: #c9b79c;
  }
  * { margin: 0; padding: 0; box-sizing: border-box; }
  html, body { width: 900px; height: 1200px; overflow: hidden; }
  body { background: var(--backdrop); position: relative; font-family: "Lato", sans-serif; }

  .card { position: absolute; left: 78px; width: 746px; height: 318px; overflow: hidden; background: var(--paper); }
  .card--front { top: 235px; }
  .card--back { top: 612px; }
  .card__art { position: absolute; inset: 0; }

  .headline { position: absolute; left: 29px; top: 22px; white-space: nowrap; }
  .headline__title { font-family: "Bebas Neue", sans-serif; font-weight: 400; font-size: 31px; line-height: 1; letter-spacing: 0.1px; }
  .headline__tagline { font-weight: 700; font-size: 15.5px; line-height: 1.2; letter-spacing: 0.2px; margin-top: 3px; }
  .card--front .headline__title { color: var(--white); }
  .card--front .headline__tagline { color: var(--orange); }
  .card--back .headline__title { color: var(--black); }
  .card--back .headline__tagline { color: var(--white); }

  .price-tag { position: absolute; left: 562px; top: 16px; width: 160px; text-align: center; color: var(--white); font-family: "Crimson Text", serif; line-height: 0.95; }
  .price-tag__small { font-size: 27px; }
  .price-tag__big { font-size: 39px; }

  .gift-title { position: absolute; left: 330px; top: 122px; font-family: "Bebas Neue", sans-serif; font-weight: 400; font-size: 37px; line-height: 1; color: var(--orange); letter-spacing: 0.5px; }

  .clinic-name { position: absolute; font-weight: 400; font-size: 13px; letter-spacing: 0.6px; line-height: 1.35; text-transform: uppercase; }
  .card--front .clinic-name { left: 86px; top: 236px; color: var(--white); }
  .card--back .clinic-name { left: 87px; top: 226px; color: var(--ink); }

  .contact { position: absolute; left: 269px; top: 128px; font-family: "Crimson Text", serif; font-style: normal; color: var(--ink); }
  .contact__address { font-size: 21px; line-height: 1.3; margin-bottom: 12px; }
  .contact__line { font-size: 16.5px; line-height: 1.4; }
  .contact__label { color: var(--orange); }
</style>
</head>
<body>

<section class="card card--front" aria-label="Gift certificate front">
  <svg class="card__art" width="746" height="318" viewBox="0 0 746 318">
    <defs>
      <linearGradient id="paperFront" x1="0" y1="0" x2="0" y2="1">
        <stop offset="0" stop-color="#f7f7f7"/><stop offset="1" stop-color="#d4d4d4"/>
      </linearGradient>
      <linearGradient id="orangePanel" x1="0" y1="0" x2="1" y2="1">
        <stop offset="0" stop-color="#ff9a3c"/><stop offset="1" stop-color="#ef5a10"/>
      </linearGradient>
      <linearGradient id="photoTone" x1="0" y1="0" x2="1" y2="1">
        <stop offset="0" stop-color="#8fb3d6"/><stop offset="1" stop-color="#d8b69a"/>
      </linearGradient>
    </defs>
    <rect class="paper" width="746" height="318" fill="url(#paperFront)"/>
    <path class="orange-panel" d="M0 86 C90 80 180 86 250 96 C292 140 300 230 268 287 L0 287 Z" fill="url(#orangePanel)"/>
    <path class="panel-edge" d="M250 96 C292 140 300 230 268 287" fill="none" stroke="var(--black)" stroke-width="9"/>
    <path class="wave-stripe" d="M0 78 C120 74 220 84 300 94 C420 102 600 98 746 92 L746 104 C600 108 420 110 300 104 C220 96 120 86 0 88 Z" fill="var(--orange)"/>
    <path class="wave-highlight" d="M0 88 C120 86 220 96 300 104 C420 110 600 108 746 104" fill="none" stroke="var(--white)" stroke-width="2"/>
    <path class="top-band" d="M0 0 H746 V92 C600 98 420 102 300 94 C220 84 120 74 0 78 Z" fill="var(--black)"/>
    <g role="img" aria-label="Photo of a smiling family outdoors">
      <circle cx="227" cy="152" r="38" fill="var(--white)"/>
      <circle cx="227" cy="152" r="34" fill="url(#photoTone)" stroke="var(--orange)" stroke-width="3"/>
    </g>
    <g role="img" aria-label="Photo of a parent hugging a child">
      <circle cx="274" cy="230" r="38" fill="var(--white)"/>
      <circle cx="274" cy="230" r="34" fill="url(#photoTone)" stroke="var(--orange)" stroke-width="3"/>
    </g>
    <g class="write-lines" stroke="#555" stroke-width="1" stroke-dasharray="5 3">
      <line x1="330" y1="186" x2="705" y2="186"/>
      <line x1="330" y1="225" x2="705" y2="225"/>
      <line x1="330" y1="262" x2="705" y2="262"/>
    </g>
    <rect class="footer-rule" y="285" width="746" height="3" fill="var(--orange)"/>
    <rect class="footer-band" y="288" width="746" height="30" fill="var(--black)"/>
    <path class="price-tag-shadow" d="M562 0 H722 V126 Q722 138 710 138 H574 Q562 138 562 126 Z" fill="var(--orange-deep)" opacity="0.45" transform="translate(3 4)"/>
    <path class="price-tag-shape" d="M562 0 H722 V126 Q722 138 710 138 H574 Q562 138 562 126 Z" fill="var(--orange)"/>
  </svg>

  <div class="headline">
    <h1 class="headline__title">Massage Certificate for our Chiropractic Office</h1>
    <p class="headline__tagline">WE CARE FOR KIDS AND FAMILIES, AND PROVIDE VITALITY CARE</p>
  </div>
  <div class="price-tag">
    <div class="price-tag__small">MASSAGE</div>
    <div class="price-tag__big">PRICE</div>
    <div class="price-tag__big">OF $50</div>
  </div>
  <h2 class="gift-title">Gift Certificate</h2>
  <p class="clinic-name">Desert Ridge Family<br>Chiropractic</p>
</section>

<section class="card card--back" aria-label="Gift certificate back">
  <svg class="card__art" width="746" height="318" viewBox="0 0 746 318">
    <defs>
      <linearGradient id="paperBack" x1="0" y1="0" x2="0" y2="1">
        <stop offset="0" stop-color="#f4f4f4"/><stop offset="1" stop-color="#d0d0d0"/>
      </linearGradient>
      <linearGradient id="orangeBand" x1="0" y1="0" x2="1" y2="0">
        <stop offset="0" stop-color="#ff9a3c"/><stop offset="1" stop-color="#f06010"/>
      </linearGradient>
      <linearGradient id="mapTone" x1="0" y1="0" x2="1" y2="1">
        <stop offset="0" stop-color="#e4e0d8"/><stop offset="1" stop-color="#cfc9bd"/>
      </linearGradient>
    </defs>
    <rect class="paper" width="746" height="318" fill="url(#paperBack)"/>
    <path class="top-band" d="M0 0 H746 V76 C600 82 420 88 300 92 C200 95 100 90 0 78 Z" fill="url(#orangeBand)"/>
    <path class="band-edge" d="M0 78 C100 90 200 95 300 92 C420 88 600 82 746 76" fill="none" stroke="var(--black)" stroke-width="5"/>
    <line class="divider" x1="243" y1="110" x2="243" y2="270" stroke="#bdbdbd" stroke-width="1.5"/>
    <circle class="map-ring" cx="657" cy="133" r="122" fill="var(--black)"/>
    <circle class="map-ring-accent" cx="657" cy="133" r="117" fill="var(--orange)"/>
    <circle cx="657" cy="133" r="112" fill="url(#mapTone)" role="img" aria-label="Street map showing the office location"/>
    <g class="map-pin" transform="translate(668 62)">
      <path d="M0 0 C-9 0 -15 7 -15 15 C-15 26 0 40 0 40 C0 40 15 26 15 15 C15 7 9 0 0 0 Z" fill="#d9362b"/>
      <circle cx="0" cy="15" r="5" fill="#8a1c14"/>
    </g>
    <rect class="footer-rule" y="285" width="746" height="3" fill="var(--orange)"/>
    <rect class="footer-band" y="288" width="746" height="30" fill="var(--black)"/>
  </svg>

  <div class="headline">
    <h2 class="headline__title">Massage Certificate for our Chiropractic Office</h2>
    <p class="headline__tagline">WE CARE FOR KIDS AND FAMILIES, AND PROVIDE VITALITY CARE</p>
  </div>
  <p class="clinic-name">Desert Ridge Family<br>Chiropractic</p>
  <address class="contact">
    <p class="contact__address">4173 W. Marlow Lane,<br>C204, Scottsdale, AZ 85260.</p>
    <p class="contact__line"><span class="contact__label">Phone:</span> (480) 731-2946</p>
    <p class="contact__line"><span class="contact__label">Fax:</span> (480) 731-2950</p>
    <p class="contact__line"><span class="contact__label">Email:</span> info@desertridgefamilychiro.com</p>
  </address>
</section>

</body>
</html>
```